Business Card Design

My business is writing crime novels to entertain readers. I write legal thrillers and mysteries. I need a card for publishers, agents, other authors, and media.

Industry/Entity Type

Legal

Contact Information for Business Card

Paul Ostrander
www.ostranderthrillers.example
paulbostrander@mailbox.example
0064 27 5139427

```html
<!DOCTYPE html>
<html lang="en">
<head>
<meta charset="utf-8">
<title>Paul Ostrander – Business Card</title>
<link rel="stylesheet" href="https://fonts.googleapis.com/css2?family=Tinos&display=swap">
<style>
  :root {
    --card-black: #0b0b0b;
    --card-grain: #151515;
    --stroke-tone: #1e1e1e;
    --ink-white: #f4f4f4;
    --portrait-dark: #1a1a1a;
    --portrait-mid: #3a3835;
    --portrait-light: #8a7f78;
  }
  html, body {
    margin: 0;
    padding: 0;
    width: 1200px;
    height: 741px;
    overflow: hidden;
    background: var(--card-black);
  }
  .card {
    position: relative;
    width: 1200px;
    height: 741px;
    overflow: hidden;
    background:
      repeating-linear-gradient(90deg, var(--card-grain) 0 1px, transparent 1px 4px),
      var(--card-black);
    font-family: "Tinos", "Times New Roman", serif;
    color: var(--ink-white);
  }
  .brush-texture {
    position: absolute;
    left: 0;
    top: 0;
    width: 560px;
    height: 741px;
  }
  .author-portrait {
    position: absolute;
    left: 738px;
    top: 76px;
    width: 462px;
    height: 665px;
  }
  .author-name {
    position: absolute;
    left: 288px;
    top: 328px;
    margin: 0;
    font-weight: 400;
    font-size: 56px;
    line-height: 1;
    font-variant: small-caps;
    letter-spacing: 5px;
    white-space: nowrap;
  }
  .contact-list {
    position: absolute;
    left: 71px;
    top: 524px;
    margin: 0;
    padding: 0;
    list-style: none;
    font-size: 28px;
    line-height: 48px;
    letter-spacing: 0.3px;
  }
</style>
</head>
<body>
  <div class="card">
    <svg class="brush-texture" viewBox="0 0 560 741" role="img" aria-label="Faint dark brush-stroke texture">
      <defs>
        <linearGradient id="strokeFade" x1="0" y1="0" x2="1" y2="0">
          <stop offset="0" stop-color="var(--stroke-tone)" stop-opacity="0.9"/>
          <stop offset="1" stop-color="var(--stroke-tone)" stop-opacity="0"/>
        </linearGradient>
      </defs>
      <rect width="560" height="741" fill="url(#strokeFade)"/>
    </svg>

    <svg class="author-portrait" viewBox="0 0 462 665" role="img" aria-label="Portrait photograph of the author in a white shirt and black leather jacket">
      <defs>
        <radialGradient id="portraitTone" cx="0.5" cy="0.3" r="0.75">
          <stop offset="0" stop-color="var(--portrait-light)"/>
          <stop offset="0.45" stop-color="var(--portrait-mid)"/>
          <stop offset="1" stop-color="var(--portrait-dark)"/>
        </radialGradient>
      </defs>
      <rect width="462" height="665" fill="url(#portraitTone)"/>
    </svg>

    <h1 class="author-name">Paul Ostrander</h1>

    <ul class="contact-list">
      <li>Website : www.ostranderthrillers.example</li>
      <li>Email : paulbostrander@mailbox.example</li>
      <li>Tel : 0064 27 5139427</li>
    </ul>
  </div>
</body>
</html>
```